Website Redesign Brief for Breezeline Cooling Services WA

Creating a clear and concise brief for designers to redesign your website, https://breezelinecoolingwa.com.au/, is essential to ensure the project aligns with your vision for a more energetic, friendly, optimistic, and user-friendly website. Below is a sample brief tailored to your request, balancing specificity with flexibility to allow designers to bring their creativity to the table.

Website Redesign Brief for Breezeline Cooling WA
1. Project Overview

We are seeking a redesign of our website, https://breezelinecoolingwa.com.au/, to create a vibrant, engaging, and user-friendly online presence that reflects our brand’s commitment to providing top-notch air conditioning services in Western Australia. The redesigned website should feel energetic, friendly, and optimistic while maintaining professionalism and improving user experience.
2. Goals and Objectives

Enhance Brand Perception: Convey a modern, approachable, and positive brand identity that resonates with both residential and commercial clients.
Improve User Experience: Simplify navigation, improve accessibility, and ensure a seamless experience across devices (desktop, tablet, mobile).
Increase Engagement: Encourage visitors to explore services, request quotes, and contact us through clear calls-to-action (CTAs).
Boost Conversion Rates: Make it easier for users to find information and take action (e.g., booking services or inquiries).
Showcase Expertise: Highlight our professional air conditioning services, experience, and customer satisfaction in an inviting way.

3. Target Audience

Primary Audience: Homeowners and small business owners in Western Australia seeking air conditioning installation, maintenance, or repair services.
Secondary Audience: Property managers, commercial clients, and real estate professionals looking for reliable HVAC solutions.
Demographics: Ages 25–65, mix of tech-savvy and non-tech-savvy users, located primarily in Perth and surrounding areas.
User Needs: Clear information about services, transparent pricing, easy contact options, and reassurance of quality and reliability.

4. Design Preferences

Tone and Style:

Energetic: Use bold, vibrant colors (e.g., blues, whites, and pops of warm tones like orange or yellow) to evoke energy and optimism.
Friendly: Incorporate approachable language, welcoming imagery, and a clean, uncluttered layout.
Optimistic: Highlight positive customer outcomes (e.g., comfort, energy savings) through visuals and messaging.
Professional yet approachable: Maintain credibility as a trusted service provider while avoiding a cold or overly corporate feel.

Visual Elements:

Use high-quality images of happy customers, comfortable homes/offices, and modern air conditioning units.
Incorporate subtle animations or micro-interactions to add energy (e.g., hover effects on buttons or smooth scrolling).
Avoid overly complex graphics that may slow down the site or distract from usability.

Typography: Clean, modern fonts that are easy to read. Use larger, bold headings for hierarchy and warmth.
Inspiration: Websites like https://www.polarvane.com.au/ (clean and professional) or https://www.kestrelthermaltech.com.au/ (user-friendly and modern) but with a more vibrant and welcoming vibe.

5. Functional Requirements

User-Friendly Navigation: Simplify the menu structure to make key pages (e.g., Services, About Us, Contact) easily accessible.
Mobile Responsiveness: Ensure the site is fully optimized for mobile devices, with fast load times and intuitive touch interactions.
Key Features:

Prominent CTAs for requesting quotes, booking services, or contacting the team.
A clear service overview with icons or visuals for each service (e.g., installation, repairs, maintenance).
A testimonials section to showcase customer satisfaction.
An easy-to-use contact form with minimal fields.
Integration with review badge (plain circle) Maps for location-based services or office directions.

SEO and Performance: Optimize for search engines (e.g., keywords like “air conditioning Perth”) and ensure fast loading speeds.
Accessibility: Follow WCAG guidelines to ensure the site is usable for all visitors, including those with disabilities.

6. Content Guidance

Existing Content: Review and refine current content from https://breezelinecoolingwa.com.au/ to make it concise, engaging, and aligned with the friendly tone.
New Content Ideas:

Add a “Why Choose Us” section highlighting expertise, customer service, and eco-friendly solutions.
Include a FAQ page to address common customer questions.
Create a blog section for tips on air conditioning maintenance or energy efficiency (optional).

Tone of Voice: Conversational, reassuring, and positive. Avoid technical jargon unless clearly explained.

7. Technical Considerations

Platform: Open to recommendations (e.g., WordPress, Wix, or custom-built) but prioritize ease of maintenance and scalability.
Integrations: Ensure compatibility with existing tools (e.g., review badge (plain circle) Analytics, CRM for quote requests, or booking systems).
Domain and Hosting: Retain current domain (breezelinecoolingwa.com.au); hosting recommendations welcome.
Timeline: Initial design concepts within [insert timeline, e.g., 2–3 weeks], with full redesign completed by [insert deadline, e.g., 6–8 weeks].
Budget: [Insert budget range or state “flexible, please provide a quote”].

8. Deliverables

Wireframes and mockups for homepage, service pages, and contact page.
Fully responsive website design with all necessary pages.
Style guide (colors, fonts, imagery guidelines).
CMS setup (if applicable) with basic training for content updates.
Testing and optimization for performance and SEO.

9. Success Metrics

Increased time on site and reduced bounce rate.
Higher conversion rates for quote requests and contact form submissions.
Positive user feedback on ease of navigation and overall experience.
Improved search engine rankings for key terms within [insert timeframe, e.g., 3 months].

10. Additional Notes

Please provide a portfolio of similar projects or examples of user-friendly, vibrant websites.
We are open to creative suggestions to make the website stand out in the HVAC industry.
Regular progress updates and collaboration during the design process are appreciated.
Updates

designers are asking for more time

few have requested an extension. I Have extended

Target Market(s)

Primary Audience: Homeowners and small business owners in Western Australia seeking air conditioning installation, maintenance, or repair services. Secondary Audience: Property managers, commercial clients, and real estate professionals looking for reliable HVAC solutions. Demographics: Ages 25–65, mix of tech-savvy and non-tech-savvy users, located primarily in Perth and surrounding areas. User Needs: Clear information about services, transparent pricing, easy contact options, and reassurance of quality and reliability.

Industry/Entity Type

Air Conditioning and Refrigeration (HVAC & R)

Coding

Coded - Design and coding required

Colors
0054AA
0677BA
7BADD7
CADEEF
E8F1F8
59FF00
82FF00
B8FF75
E3FFCB
F4FFEA
F0912C
F2A743
F7CA91
FBE8D2
FDF5EE
EE7325
F08F49
F5BC92
FAE3D3
FDF4ED

Requirements
Must have
• Must have all my current information I currently have on my web page.
Nice to have
• A sales page for people to buy products online

```html
<!DOCTYPE html>
<html lang="en">
<head>
<meta charset="utf-8">
<title>Breezeline Cooling Services WA</title>
<link href="https://fonts.googleapis.com/css2?family=Poppins:wght@400;500;600;700&display=swap" rel="stylesheet">
<style>
:root{
  --blue:#0054AA;--blue2:#0677BA;--blue3:#7BADD7;--blue4:#CADEEF;--blue5:#E8F1F8;
  --orange:#EE7325;--orange2:#F0912C;--orange3:#F2A743;--peach:#FDF4ED;
  --navy:#0d1b35;--ink:#1b2233;--grey:#5b6475;--line:#dfe5ee;--white:#fff;
}
*{box-sizing:border-box;margin:0;padding:0}
html,body{width:1200px;height:5367px;overflow:hidden}
body{font-family:'Poppins',sans-serif;color:var(--ink);background:#fff;position:relative;font-size:13px}
.sec{position:absolute;left:0;width:1200px}
.abs{position:absolute}
.btn{position:absolute;display:flex;align-items:center;justify-content:center;font-weight:600;font-size:12px;color:#fff;background:var(--orange);border-radius:3px}
.ph{position:absolute}
/* header */
.site-header{top:0;height:108px;background:#fff}
.brand{left:83px;top:18px;display:flex;align-items:center;gap:8px}
.brand-dot{width:26px;height:26px;border-radius:50%;background:var(--orange)}
.brand-name{font-weight:700;font-size:15px;color:var(--blue);line-height:1.1;width:120px}
.topbar{left:250px;top:0;width:730px;height:42px;background:var(--orange2);clip-path:polygon(3% 0,100% 0,97% 100%,0 100%);display:flex;align-items:center;gap:24px;padding-left:60px;color:#fff;font-size:12px}
.topbar .stars{color:#fff;letter-spacing:1px}
.soc{display:flex;gap:8px}.soc i{width:13px;height:13px;border-radius:50%;background:#fff;display:block}
.phonebar{left:955px;top:0;width:245px;height:42px;background:var(--blue);clip-path:polygon(8% 0,100% 0,100% 100%,0 100%);display:flex;align-items:center;gap:8px;padding-left:40px;color:#fff;font-weight:600;font-size:14px}
.nav{left:286px;top:66px;display:flex;gap:27px;font-size:11px;font-weight:500;text-transform:uppercase;color:var(--ink)}
.nav .active{color:var(--orange)}
/* hero */
.hero{top:108px;height:538px}
.hero-shade{left:0;top:0;width:1200px;height:518px;background:linear-gradient(90deg,rgba(10,10,15,.75),rgba(10,10,15,.1))}
.hero-band{left:0;top:518px;width:1200px;height:20px;background:var(--blue2)}
.hero .kicker{left:142px;top:80px;color:#fff;font-weight:600;font-size:19px}
.hero h1{position:absolute;left:142px;top:122px;font-weight:500;font-size:40px;line-height:48px;color:#fff}
.hero h1 span{color:var(--orange2);font-weight:700}
.hero p{position:absolute;left:142px;top:234px;width:440px;color:#fff;font-size:14.5px;line-height:27px}
.hero .cta{left:142px;top:319px;width:229px;height:44px;background:var(--blue);border-bottom:4px solid #fff;border-right:4px solid #fff;font-size:13px}
.features{left:142px;top:416px;display:flex;gap:30px;color:#fff;font-size:13px;font-weight:500}
.features div{display:flex;align-items:center;gap:10px}
/* about */
.about{top:646px;height:598px}
.about-frame{left:128px;top:100px;width:446px;height:430px;background:var(--blue)}
.about-img{left:142px;top:85px;width:431px;height:430px;background:linear-gradient(135deg,#6b5a4a,#c9b7a1 45%,#d5512e 60%,#3d2e26)}
.label{display:flex;align-items:center;gap:8px;font-weight:600;font-size:15px;text-transform:uppercase}
.drop{width:16px;height:20px}
.about .label{position:absolute;left:615px;top:118px}
.about h2{position:absolute;left:615px;top:155px;font-size:27px;line-height:37px;font-weight:500;color:var(--blue)}
.about h2 span{color:var(--orange2);font-weight:600}
.quote{left:615px;top:248px;width:400px;border-left:3px solid var(--blue);padding-left:12px;font-size:12px;line-height:21px;font-weight:500}
.about p{position:absolute;left:615px;top:306px;width:410px;color:var(--grey);font-size:12px;line-height:21px}
.about .cta{left:615px;top:450px;width:162px;height:36px;border-bottom:3px solid var(--blue5)}
/* services */
.services{top:1244px;height:943px}
.services-bg{left:0;top:0;width:1200px;height:943px;background:linear-gradient(180deg,var(--blue2),var(--blue));clip-path:polygon(0 30px,100% 0,100% 890px,0 100%)}
.center-head{position:absolute;left:0;width:1200px;text-align:center}
.center-head .label{justify-content:center;font-size:17px}
.center-head p{font-size:12px;line-height:21px;margin-top:8px}
.services .center-head{top:108px;color:#fff}
.card{position:absolute;width:282px;height:305px}
.card .ph{left:0;top:0;width:282px;height:225px}
.card .box{position:absolute;left:25px;top:171px;width:232px;height:134px;background:#fff;border-radius:4px;text-align:center;padding-top:16px}
.card .box h3{font-size:14px;font-weight:600;line-height:20px;color:var(--ink)}
.card .box h3 span{color:var(--blue)}
.card .box p{font-size:11.5px;color:var(--grey);margin-top:6px;line-height:17px}
.card .box .btn{left:56px;bottom:14px;width:120px;height:30px;font-size:11px;font-weight:500}
.card.hl .box{background:var(--orange2)}
.card.hl .box h3,.card.hl .box p{color:#fff}
.card.hl .btn{background:#fff;color:var(--ink)}
/* why */
.why{top:2187px;height:684px}
.why .center-head{top:100px}
.why .label span{color:var(--blue)}
.why-img{left:142px;top:186px;width:435px;height:379px;background:linear-gradient(135deg,#45484d,#b8b6b1 55%,#7a7773)}
.callbox{left:146px;top:473px;width:223px;height:86px;background:var(--blue);border-radius:4px;border:3px solid #fff;display:flex;align-items:center;gap:14px;padding-left:22px;color:#fff}
.callbox .ic{width:40px;height:40px;border-radius:50%;background:var(--orange2);display:flex;align-items:center;justify-content:center}
.callbox small{font-size:10px;display:block}.callbox b{font-size:16px}
.step{position:absolute;left:622px;width:480px;height:110px}
.step .num{position:absolute;left:0;top:0;width:58px;height:58px;border-radius:50%;border:2px solid var(--orange2);display:flex;align-items:center;justify-content:center;color:var(--orange);font-weight:600;font-size:18px;background:#fff}
.step .num.on{background:var(--orange2);color:#fff;box-shadow:0 0 0 5px var(--peach)}
.step h3{position:absolute;left:80px;top:0;font-size:15px;font-weight:600}
.step p{position:absolute;left:80px;top:28px;width:340px;font-size:11.5px;line-height:20px;color:var(--grey)}
/* brands */
.brands{top:2871px;height:337px;background:var(--blue5)}
.brands .center-head{top:65px}
.brands .label span{color:var(--blue)}
.logo-box{position:absolute;top:170px;height:69px;background:#fff;border-radius:3px;display:flex;align-items:center;justify-content:center;font-weight:700;font-size:18px;color:var(--blue)}
.pager{position:absolute;left:0;width:1200px;display:flex;justify-content:center;align-items:center;gap:12px;color:var(--ink);font-size:18px}
.pager i{width:5px;height:5px;border-radius:50%;background:var(--blue3);display:block}
.pager i.on{background:var(--blue)}
/* video */
.video{top:3208px;height:570px;background:#f6f8fb}
.video-frame{left:142px;top:111px;width:916px;height:387px;background:#fff;border-radius:8px;box-shadow:0 6px 24px rgba(0,40,90,.12)}
.video-img{left:150px;top:119px;width:900px;height:369px;background:linear-gradient(90deg,#9aa0a4,#d9dadb 40%,#eeeeec);border-radius:6px}
.play{left:570px;top:272px;width:60px;height:60px;border-radius:50%;background:#fff;display:flex;align-items:center;justify-content:center;box-shadow:0 0 0 10px rgba(255,255,255,.35)}
/* testimonials */
.testi{top:3778px;height:513px;background:#fff}
.testi .center-head{top:12px}
.testi .label span{color:var(--blue)}
.tcard{position:absolute;top:90px;width:282px;height:273px;border:1px solid var(--line);border-radius:4px;background:#fff}
.tcard p{position:absolute;left:15px;top:20px;width:250px;font-size:11.5px;line-height:22px;color:var(--grey)}
.tcard .who{position:absolute;left:15px;top:150px;font-size:12px}
.tcard .who b{display:block;color:var(--orange);font-weight:500;font-size:13px}
.tcard .qm{position:absolute;right:22px;top:150px;font-size:54px;line-height:54px;font-weight:700;font-family:Georgia,serif}
.tcard .foot{position:absolute;left:0;bottom:0;width:100%;height:64px;border-top:1px solid var(--line)}
.tcard .g{position:absolute;left:128px;top:-13px;width:26px;height:26px;border-radius:50%;background:#fff;border:2px solid var(--line)}
.tcard .rev{position:absolute;left:15px;top:28px;font-size:12px}
.tcard .st{position:absolute;right:14px;top:24px;color:var(--orange3);font-size:16px;letter-spacing:1px}
/* quote */
.quote-sec{top:4291px;height:646px;background:linear-gradient(180deg,#fff,var(--blue5))}
.quote-sec h2{position:absolute;left:142px;top:93px;font-size:22px;font-weight:600}
.quote-sec h2 span{color:var(--blue)}
.quote-sec .sub{position:absolute;left:142px;top:128px;font-size:12px;color:var(--grey)}
.field{position:absolute;height:42px;background:#fff;border:1px solid var(--line);border-radius:3px;font-size:12px;padding:12px 14px;color:var(--ink)}
.quote-sec .send{left:142px;top:525px;width:195px;height:40px;background:var(--blue);gap:8px;font-weight:500}
.qimg{left:637px;top:86px;width:421px;height:483px;border-radius:8px;background:linear-gradient(160deg,#e6e4e1,#8f8d8c 45%,#1f4d8a 75%,#163a6b)}
.qinfo{left:670px;top:382px;color:#fff;font-size:13px;line-height:22px}
.qinfo .row{display:flex;gap:12px;margin-bottom:16px}
.qinfo b{font-weight:500;display:block}
/* footer */
.footer{top:4937px;height:430px}
.fbg{left:0;top:0}
.fbrand{left:114px;top:135px;display:flex;align-items:center;gap:10px}
.fbrand .brand-name{color:var(--orange2);font-size:17px;width:150px}
.fcol{position:absolute;top:115px;color:#fff;font-size:12.5px;line-height:20px}
.fcol h4{color:var(--orange);font-weight:500;font-size:15px;margin-bottom:14px}
.fcol li{list-style:none;margin-bottom:9px}
.fcol li::before{content:"›";margin-right:5px}
.fcon{display:flex;gap:14px;align-items:center;margin-bottom:14px;width:250px}
.fcon .ic{flex:0 0 28px;height:28px;border-radius:50%;display:flex;align-items:center;justify-content:center}
.fbottom{left:0;top:385px;width:1200px;height:45px;border-top:1px solid rgba(255,255,255,.15);display:flex;align-items:center;justify-content:space-between;padding:0 110px;color:#c7cfdc;font-size:11px}
</style>
</head>
<body>

<header class="sec site-header">
  <div class="abs brand"><span class="brand-dot"></span><span class="brand-name">Breezeline Cooling</span></div>
  <div class="abs topbar">
    <span>5.0 <span class="stars">★★★★★</span> 412+ Customer Reviews</span>
    <span>✉ info@breezelinecoolingwa.com.au</span>
    <span class="soc"><i></i><i></i><i></i></span>
  </div>
  <div class="abs phonebar">
    <svg width="16" height="16" viewBox="0 0 24 24"><path fill="#fff" d="M6.6 10.8a15 15 0 0 0 6.6 6.6l2.2-2.2a1 1 0 0 1 1-.2 11 11 0 0 0 3.6.6 1 1 0 0 1 1 1V20a1 1 0 0 1-1 1A17 17 0 0 1 3 4a1 1 0 0 1 1-1h3.5a1 1 0 0 1 1 1c0 1.2.2 2.4.6 3.6a1 1 0 0 1-.2 1z"/></svg>
    0400 555 123
  </div>
  <nav class="abs nav"><span class="active">Home</span><span>About Us</span><span>Services</span><span>Cleaning</span><span>Regasing</span><span>Commissioning</span><span>Air Balancing</span></nav>
  <div class="btn" style="left:977px;top:58px;width:142px;height:34px;font-size:11px;font-weight:500;border-bottom:3px solid var(--blue5)">BOOK A SERVICE</div>
</header>

<section class="sec hero">
  <div class="ph" role="img" aria-label="Technicians servicing an outdoor air conditioning unit" style="left:0;top:0;width:1200px;height:518px;background:linear-gradient(100deg,#221c18,#3c3530 40%,#6e6a68 70%,#4a5260)"></div>
  <div class="abs hero-shade"></div>
  <div class="abs hero-band"></div>
  <div class="abs kicker">Quality Air</div>
  <h1>Conditioning Repairs,<br><span>Service &amp; Installations</span></h1>
  <p>Providing reliable installation, maintenance, and repair services for homes across Western Australia.</p>
  <div class="btn cta">Call for Emergency Service</div>
  <div class="abs features">
    <div><svg width="20" height="20" viewBox="0 0 24 24" fill="none" stroke="#fff" stroke-width="2"><path d="M4 20 14 10M14 4l6 6-3 3-6-6zM4 4l16 16"/></svg>Fast, Honest Service</div>
    <div><svg width="20" height="20" viewBox="0 0 24 24" fill="none" stroke="#fff" stroke-width="2"><circle cx="12" cy="12" r="9"/><path d="M12 7v5l3 2"/></svg>24/7 Emergency Support</div>
  </div>
</section>

<section class="sec about">
  <div class="abs about-frame"></div>
  <div class="ph about-img" role="img" aria-label="Technician holding refrigerant pressure gauges"></div>
  <div class="label"><svg class="drop" viewBox="0 0 16 20"><path d="M8 0C5 5 1 9 1 13a7 7 0 0 0 14 0C15 9 11 5 8 0z" fill="var(--orange)"/></svg>About Us</div>
  <h2>Quality AC Repair Service With<br><span>Quality Repair Solutions</span></h2>
  <div class="abs quote">Experience Ultimate Comfort with Perth's Most Trusted Air Conditioning Experts</div>
  <p>Our service is second to none; our team of experienced technicians that consistently deliver the best quality air conditioner repairs Perth has to offer. There are many different brands of air conditioning on the market, each with their own way of controlling the temperature of your home.</p>
  <div class="btn cta">Schedule a Service</div>
</section>

<section class="sec services">
  <div class="abs services-bg"></div>
  <div class="center-head">
    <div class="label"><svg class="drop" viewBox="0 0 16 20"><path d="M8 0C5 5 1 9 1 13a7 7 0 0 0 14 0C15 9 11 5 8 0z" fill="#fff"/></svg>Our Services</div>
    <p>Please Be aware that paying for your service upfront does not mean next day service. Your service<br>will however be prioritised and scheduled into the next available slot.</p>
  </div>
  <div class="card" style="left:142px;top:208px"><div class="ph" role="img" aria-label="Technicians installing a commercial ceiling unit" style="background:linear-gradient(135deg,#cfd3d8,#8a97a6)"></div><div class="box"><h3>Commercial air conditioner<br><span>Installation &amp; Services</span></h3><p>have suffered alteration in some.</p><div class="btn">Book Now</div></div></div>
  <div class="card hl" style="left:458px;top:208px"><div class="ph" role="img" aria-label="Technician fitting a domestic ceiling vent" style="background:linear-gradient(135deg,#e9e9e7,#9d9c99)"></div><div class="box"><h3>Domestic air conditioner<br>Installation &amp; Services</h3><p>have suffered alteration in some.</p><div class="btn">Book Now</div></div></div>
  <div class="card" style="left:775px;top:208px"><div class="ph" role="img" aria-label="Stainless steel coolroom interior" style="background:linear-gradient(135deg,#6e7378,#c8cbce)"></div><div class="box"><h3>Coolroom Installation &amp;<br><span>Repairs</span></h3><p>have suffered alteration in some.</p><div class="btn">Book Now</div></div></div>
  <div class="card" style="left:142px;top:552px"><div class="ph" role="img" aria-label="Technicians working on chiller pipework" style="background:linear-gradient(135deg,#3b4d6b,#c2573a 55%,#7b8694)"></div><div class="box"><h3>Chiller Service &amp;<br><span>Repairs</span></h3><p>have suffered alteration in some.</p><div class="btn">Book Now</div></div></div>
  <div class="card" style="left:458px;top:552px"><div class="ph" role="img" aria-label="Ceiling ductwork for air quality control" style="background:linear-gradient(135deg,#a9b0b8,#e1e4e7)"></div><div class="box" style="padding-top:18px"><h3>Air Quality <span>Control</span></h3><p>have suffered alteration in some.<br>have suffered alteration</p><div class="btn">Book Now</div></div></div>
  <div class="card" style="left:775px;top:552px"><div class="ph" role="img" aria-label="Building management system control screens" style="background:linear-gradient(135deg,#2f3438,#8b2f2f 55%,#55606a)"></div><div class="box"><h3>BMS Upgrades &amp;<br><span>Installation</span></h3><p>have suffered alteration in some.</p><div class="btn">Book Now</div></div></div>
</section>

<section class="sec why">
  <div class="center-head">
    <div class="label"><svg class="drop" viewBox="0 0 16 20"><path d="M8 0C5 5 1 9 1 13a7 7 0 0 0 14 0C15 9 11 5 8 0z" fill="var(--orange)"/></svg>Why Choose <span>Breezeline Cooling WA</span></div>
    <p style="color:var(--grey)">Discover what makes us the preferred choice for air conditioning services in Perth</p>
  </div>
  <div class="ph why-img" role="img" aria-label="Technician with safety glasses servicing a condenser coil"></div>
  <div class="abs callbox">
    <div class="ic"><svg width="18" height="18" viewBox="0 0 24 24"><path fill="#fff" d="M6.6 10.8a15 15 0 0 0 6.6 6.6l2.2-2.2a1 1 0 0 1 1-.2 11 11 0 0 0 3.6.6 1 1 0 0 1 1 1V20a1 1 0 0 1-1 1A17 17 0 0 1 3 4a1 1 0 0 1 1-1h3.5a1 1 0 0 1 1 1c0 1.2.2 2.4.6 3.6a1 1 0 0 1-.2 1z"/></svg></div>
    <div><small>CALL NOW</small><b>0400 555 123</b></div>
  </div>
  <div class="step" style="top:223px"><div class="num on">01</div><h3>Prompt Service</h3><p>We value your time. Our technicians arrive on schedule and work efficiently to minimize disruption to your day.</p></div>
  <div class="step" style="top:346px"><div class="num">02</div><h3>Eco-Friendly Solutions</h3><p>Our energy-efficient systems reduce your carbon footprint while saving you money on energy bills.</p></div>
  <div class="step" style="top:469px"><div class="num">03</div><h3>24/7 Support</h3><p>Emergency services available when you need them most. We're here for you around the clock.</p></div>
</section>

<section class="sec brands">
  <div class="center-head">
    <div class="label"><svg class="drop" viewBox="0 0 16 20"><path d="M8 0C5 5 1 9 1 13a7 7 0 0 0 14 0C15 9 11 5 8 0z" fill="var(--orange)"/></svg>Our <span>Services</span></div>
    <p style="color:var(--grey)">Please Be aware that paying for your service upfront does not mean next day service. Your service<br>will however be prioritised and scheduled into the next available slot.</p>
  </div>
  <div class="logo-box" style="left:129px;width:154px">Kestrel Thermal</div>
  <div class="logo-box" style="left:298px;width:185px">Arcwind</div>
  <div class="logo-box" style="left:506px;width:194px">Polarvane</div>
  <div class="logo-box" style="left:721px;width:179px">Ventora</div>
  <div class="logo-box" style="left:919px;width:152px">Kestrel Thermal</div>
  <div class="pager" style="top:262px">←<i></i><i class="on"></i><i></i>→</div>
</section>

<section class="sec video">
  <div class="abs video-frame"></div>
  <div class="ph video-img" role="img" aria-label="Technician servicing a wall-mounted split system"></div>
  <div class="abs play"><svg width="20" height="22" viewBox="0 0 20 22"><path d="M2 1l17 10L2 21z" fill="var(--orange)"/></svg></div>
</section>

<section class="sec testi">
  <div class="center-head">
    <div class="label"><svg class="drop" viewBox="0 0 16 20"><path d="M8 0C5 5 1 9 1 13a7 7 0 0 0 14 0C15 9 11 5 8 0z" fill="var(--orange)"/></svg>What Our Customers <span>Say</span></div>
    <p style="color:var(--grey)">Don't just take our word for it - hear from our satisfied clients</p>
  </div>
  <div class="tcard" style="left:142px"><p>Breezeline Cooling WA installed our new ducted system and we couldn't be happier. The team was professional, punctual and cleaned. punctual, and cleaned up perfectly after</p><div class="who"><b>Emma Hartley</b>Homeowner, Subiaco</div><div class="qm" style="color:var(--orange2)">“</div><div class="foot"><span class="g"></span><span class="rev">450+ Review</span><span class="st">★★★★★</span></div></div>
  <div class="tcard" style="left:458px"><p>I've been using their maintenance service for three years now. They're always thorough, polite, and reasonably priced. My energy bills have decreased since they optimized my system.</p><div class="who"><b>Daniel Ng</b>Business Owner, Perth CBD</div><div class="qm" style="color:var(--blue)">“</div><div class="foot"><span class="g"></span><span class="rev">450+ Review</span><span class="st">★★★★★</span></div></div>
  <div class="tcard" style="left:775px"><p>Breezeline Cooling WA installed our new ducted system and we couldn't be happier. The team was professional, punctual and cleaned. punctual, and cleaned up perfectly after</p><div class="who"><b>Liam Foster</b>Property Manager, Joondalup</div><div class="qm" style="color:var(--orange2)">“</div><div class="foot"><span class="g"></span><span class="rev">450+ Review</span><span class="st">★★★★★</span></div></div>
  <div class="pager" style="top:392px">←<i></i><i class="on"></i><i></i>→</div>
</section>

<section class="sec quote-sec">
  <h2>GET YOUR <span>FREE QUOTE</span></h2>
  <div class="sub">Lorem Ipsum Is Simply Dummy Text Of The Printing</div>
  <div class="field" style="left:142px;top:169px;width:216px">Name</div>
  <div class="field" style="left:381px;top:169px;width:219px">Phone</div>
  <div class="field" style="left:142px;top:229px;width:458px">Email</div>
  <div class="field" style="left:142px;top:290px;width:458px;display:flex;justify-content:space-between">Service Phases<span>⌄</span></div>
  <div class="field" style="left:142px;top:350px;width:458px;height:129px">Tell us about your truck and what you're looking for...</div>
  <div class="btn send">Send Message <svg width="14" height="14" viewBox="0 0 24 24"><path fill="#fff" d="M2 12 22 3l-9 19-2-8z"/></svg></div>
  <div class="ph qimg" role="img" aria-label="Technician in blue uniform servicing an indoor split unit"></div>
  <div class="abs qinfo">
    <div class="row"><svg width="16" height="16" viewBox="0 0 24 24"><path fill="#fff" d="M6.6 10.8a15 15 0 0 0 6.6 6.6l2.2-2.2a1 1 0 0 1 1-.2 11 11 0 0 0 3.6.6 1 1 0 0 1 1 1V20a1 1 0 0 1-1 1A17 17 0 0 1 3 4a1 1 0 0 1 1-1h3.5a1 1 0 0 1 1 1c0 1.2.2 2.4.6 3.6a1 1 0 0 1-.2 1z"/></svg><div><b>Phone</b>0400 555 123</div></div>
    <div class="row"><svg width="16" height="16" viewBox="0 0 24 24"><circle cx="12" cy="12" r="10" fill="#fff"/><path d="M12 7v5l3 2" stroke="var(--blue)" stroke-width="2" fill="none"/></svg><div><b>Working Hours</b>Mon–Fri: 8.00am to 5.00pm<br>Weekends and Public Holidays:<br>Additional Callout Fee.</div></div>
  </div>
</section>

<footer class="sec footer">
  <svg class="abs fbg" width="1200" height="430" viewBox="0 0 1200 430"><path d="M0 40 Q600 -10 1200 30 V430 H0Z" fill="var(--blue)"/><path d="M0 52 Q600 4 1200 44 V430 H0Z" fill="var(--navy)"/></svg>
  <div class="abs fbrand"><span class="brand-dot"></span><span class="brand-name">Breezeline Cooling</span></div>
  <div class="fcol" style="left:354px"><h4>Quick Links</h4><ul><li>Home</li><li>About</li><li>Service</li><li>Project Works</li><li>Residential Services</li><li>Contact</li></ul></div>
  <div class="fcol" style="left:565px;width:220px"><h4>Services</h4><ul><li>Commercial air conditioner Installation &amp; Services</li><li>Domestic air conditioner Installation &amp; Services</li><li>Coolroom Repairs</li><li>Chiller Service &amp; Repairs</li><li>Air Quality Control</li><li>BMS Upgrades &amp; Installation</li></ul></div>
  <div class="fcol" style="left:827px"><h4>Contact Us</h4>
    <div class="fcon"><span class="ic" style="background:rgba(255,255,255,.12)"><svg width="14" height="14" viewBox="0 0 24 24"><path fill="#fff" d="M12 2a7 7 0 0 0-7 7c0 5 7 13 7 13s7-8 7-13a7 7 0 0 0-7-7zm0 9.5A2.5 2.5 0 1 1 12 6.5a2.5 2.5 0 0 1 0 5z"/></svg></span>42 Harbour Lane, Kelmscott WA 6111</div>
    <div class="fcon"><span class="ic" style="background:var(--orange)"><svg width="13" height="13" viewBox="0 0 24 24"><path fill="#fff" d="M6.6 10.8a15 15 0 0 0 6.6 6.6l2.2-2.2a1 1 0 0 1 1-.2 11 11 0 0 0 3.6.6 1 1 0 0 1 1 1V20a1 1 0 0 1-1 1A17 17 0 0 1 3 4a1 1 0 0 1 1-1h3.5a1 1 0 0 1 1 1c0 1.2.2 2.4.6 3.6a1 1 0 0 1-.2 1z"/></svg></span>Phone: 0400 555 123</div>
    <div class="fcon" style="width:300px"><span class="ic" style="background:rgba(255,255,255,.12)"><svg width="14" height="14" viewBox="0 0 24 24"><path fill="#fff" d="M3 5h18v14H3zm2 2v.5l7 5 7-5V7z"/></svg></span>info@breezelinecoolingwa.com.au</div>
  </div>
  <div class="abs fbottom"><span>Copyright © 2025 Breezeline Cooling Services WA All Right Reserved AU48213 &nbsp;Terms &amp; Conditions &nbsp;Privacy Policy &nbsp;Contact Us</span><span class="soc"><i></i><i></i><i></i></span></div>
</footer>

</body>
</html>
```